Cannabis Company needs a packaging design for a 4x6 pouch

We need a design for a new cannabis company. Included is the logo in red. The logo color can change. Whatever color looks best with the design is what we'll use. The design can't include any cartoon characters or anything that may appeal to children. We have multiple products that are similar that will be using the same design. The pouch will contain 10 pyramid shaped gummies. The look we're going for is modern, simple, but eye catching. I included a handful of photos of packaging we like if that helps.

```html
<!DOCTYPE html>
<html lang="en">
<head>
<meta charset="utf-8">
<title>Halvora Delta-8 THC Gummies – Pouch Front</title>
<link href="https://fonts.googleapis.com/css2?family=Bebas+Neue&display=swap" rel="stylesheet">
<style>
  :root {
    --backdrop: #ebebeb;
    --pouch-deep: #6e2c20;
    --pouch-mid: #87402f;
    --pouch-glow: #c0705a;
    --ink: #f4ede6;
    --band-brown: #7d3426;
    --band-red: #a8473a;
    --band-gold: #e2a233;
  }
  * { margin: 0; padding: 0; box-sizing: border-box; }
  html, body {
    width: 1200px; height: 1200px; overflow: hidden;
    background: var(--backdrop);
  }
  .canvas {
    position: relative; width: 1200px; height: 1200px;
    font-family: "Bebas Neue", "Arial Narrow", sans-serif;
    color: var(--ink);
  }
  .pouch-front {
    position: absolute; left: 240px; top: 30px;
    width: 720px; height: 1140px;
    border-radius: 22px 22px 18px 18px;
    overflow: hidden;
    background:
      radial-gradient(ellipse 55% 30% at 58% 22%, var(--pouch-glow) 0%, rgba(192,112,90,0) 100%),
      linear-gradient(180deg, var(--pouch-mid) 0%, var(--pouch-deep) 60%, var(--pouch-mid) 100%);
  }
  .zip-seal {
    position: absolute; left: 0; right: 0; top: 138px; height: 10px;
    border-top: 2px solid rgba(0,0,0,0.18);
    border-bottom: 2px solid rgba(255,255,255,0.12);
  }
  .claims {
    position: absolute; top: 228px; width: 100%;
    text-align: center; font-size: 36px; letter-spacing: 2px;
  }
  .brand {
    position: absolute; top: 420px; width: 100%;
    display: flex; justify-content: center; align-items: center; gap: 18px;
  }
  .brand-mark {
    width: 30px; height: 30px; background: var(--ink);
  }
  .brand-name {
    font-size: 96px; letter-spacing: 4px; line-height: 1;
  }
  .product-title {
    position: absolute; top: 632px; width: 100%;
    text-align: center; font-size: 92px; line-height: 1.08; letter-spacing: 5px;
  }
  .contents {
    position: absolute; top: 856px; width: 100%;
    text-align: center; font-size: 30px; line-height: 1.05; letter-spacing: 2px;
  }
  .pattern-band {
    position: absolute; left: 0; right: 0; bottom: 0; height: 220px;
    background: linear-gradient(180deg,
      var(--band-brown) 0%, var(--band-red) 35%, var(--band-brown) 55%,
      var(--band-gold) 80%, var(--band-gold) 100%);
  }
</style>
</head>
<body>
  <main class="canvas">
    <section class="pouch-front">
      <div class="zip-seal"></div>
      <p class="claims">Gluten Free - Non GMO - Fat Free</p>
      <div class="brand">
        <span class="brand-mark"></span>
        <span class="brand-name">Halvora</span>
      </div>
      <h1 class="product-title">Delta - 8 THC<br>Gummies</h1>
      <p class="contents">10 Gummies<br>25MG Delta 8 per Gummy</p>
      <div class="pattern-band" role="img" aria-label="Zigzag chevron stripe pattern in brown, red, white and gold"></div>
    </section>
  </main>
</body>
</html>
```